Industrial Automation company requires a business card design

Dravik Automation provides design & build of Automated Equipment for manufacturing industry.
www.dravikautomation-example.com
The equipment we design is used for manufacturing in sectors such as medical device, pharmaceutical, aerospace and electronics.
We require a new business card design which incorporates our (New) logo and the key message words:
Automated Equipment:
Design, Build, Control, Test, Support

Industry/Entity Type

Business

```html
<!DOCTYPE html>
<html lang="en">
<head>
<meta charset="utf-8">
<title>Dravik Automation – Business Card</title>
<link href="https://fonts.googleapis.com/css2?family=Open+Sans:wght@400;600;700;800&display=swap" rel="stylesheet">
<style>
  :root {
    --brand-green: #0f7d3c;
    --brand-dark: #231f20;
    --card-white: #ffffff;
    --stage: #d9dcd9;
    --text-dark: #231f20;
    --text-light: #ffffff;
    --map-dot: #4a4748;
  }
  * { margin: 0; padding: 0; box-sizing: border-box; }
  html, body {
    width: 1200px; height: 900px; overflow: hidden;
    background: var(--stage);
    font-family: "Open Sans", Arial, sans-serif;
  }
  .stage { position: relative; width: 1200px; height: 900px; }

  .card {
    position: absolute;
    width: 540px; height: 310px;
    overflow: hidden;
    box-shadow: 0 10px 26px rgba(0,0,0,0.25);
  }

  /* ---------- Back side ---------- */
  .card-back { left: 70px; top: 110px; background: var(--brand-dark); }
  .card-back .world-map {
    position: absolute; left: 30px; top: 20px; width: 480px; height: 260px;
    background: radial-gradient(ellipse at center, var(--map-dot) 0%, rgba(74,71,72,0.35) 55%, rgba(35,31,32,0) 75%);
    border-radius: 40%;
  }
  .card-back .wordmark {
    position: absolute; left: 0; right: 0; top: 118px;
    text-align: center;
    font-weight: 800; font-size: 34px; letter-spacing: 2px;
    color: var(--brand-green); line-height: 1.1;
  }
  .card-back .wordmark .mark {
    display: inline-block; width: 30px; height: 30px; border-radius: 50%;
    background: var(--brand-green); vertical-align: -4px; margin-right: 10px;
  }
  .card-back .back-url {
    position: absolute; left: 150px; bottom: 34px;
    font-size: 13px; letter-spacing: 0.5px; color: var(--text-light);
  }
  .card-back .back-url .www { color: var(--brand-green); }

  /* ---------- Front side ---------- */
  .card-front { left: 590px; top: 480px; background: var(--card-white); }
  .card-front .bands { position: absolute; inset: 0; }
  .card-front .wordmark {
    position: absolute; left: 34px; top: 42px;
    font-weight: 800; font-size: 27px; letter-spacing: 1.5px;
    color: var(--brand-green); line-height: 1.1;
  }
  .card-front .wordmark .mark {
    display: inline-block; width: 26px; height: 26px; border-radius: 50%;
    background: var(--brand-green); vertical-align: -4px; margin-right: 8px;
  }
  .person {
    position: absolute; left: 340px; top: 150px; width: 180px;
    text-align: center; color: var(--text-light);
  }
  .person .name { font-weight: 700; font-size: 14px; letter-spacing: 0.3px; }
  .person .role { font-size: 13px; margin-top: 2px; }

  .contact-row {
    position: absolute; left: 22px;
    display: flex; align-items: center; gap: 10px;
    font-size: 12px; line-height: 1.3;
  }
  .contact-row .accent { width: 3px; height: 30px; background: var(--brand-green); }
  .contact-row svg { width: 16px; height: 16px; flex: none; }
  .contact-address { top: 140px; color: var(--text-dark); }
  .contact-address svg { fill: var(--text-dark); }
  .contact-phone { top: 201px; color: var(--text-light); }
  .contact-phone svg { fill: var(--text-light); }
  .contact-web { top: 256px; color: var(--text-light); }
  .contact-web .accent { background: var(--brand-dark); }
  .contact-web svg { stroke: var(--text-light); fill: none; }
</style>
</head>
<body>
<main class="stage">

  <section class="card card-back" aria-label="Business card back">
    <div class="world-map" role="img" aria-label="Dotted world map background"></div>
    <div class="wordmark"><span class="mark"></span>DRAVIK AUTOMATION</div>
    <p class="back-url"><span class="www">www.</span>dravikautomation-example.com</p>
  </section>

  <section class="card card-front" aria-label="Business card front">
    <svg class="bands" viewBox="0 0 540 310" aria-hidden="true">
      <path d="M0,193 H250 Q268,193 276,178 L316,108 Q323,95 338,95 H540 V260 H0 Z" fill="var(--brand-dark)"/>
      <path d="M0,248 H228 Q246,248 254,234 L326,120 Q334,108 350,108 H540 V292 H0 Z" fill="var(--brand-green)"/>
    </svg>

    <div class="wordmark"><span class="mark"></span>DRAVIK AUTOMATION</div>

    <div class="person">
      <p class="name">MORGAN DELANEY</p>
      <p class="role">CEO</p>
    </div>

    <div class="contact-row contact-address">
      <span class="accent"></span>
      <svg viewBox="0 0 16 16"><path d="M8 1 L15 8 H13 V15 H9.5 V10.5 H6.5 V15 H3 V8 H1 Z"/></svg>
      <p>Glenmora, Kilbrack,<br>Co. Lorne, Ireland</p>
    </div>

    <div class="contact-row contact-phone">
      <span class="accent"></span>
      <svg viewBox="0 0 16 16"><path d="M2 5 Q2 3 4 3 H12 Q14 3 14 5 V6 H11 V5 H5 V6 H2 Z M4 7 H12 L13 13 H3 Z"/></svg>
      <p>00 353 (0) 55 01234<br>00 353 (0) 55 01235</p>
    </div>

    <div class="contact-row contact-web">
      <span class="accent"></span>
      <svg viewBox="0 0 16 16" stroke-width="1.5"><rect x="1.5" y="2.5" width="13" height="9"/><path d="M6 14.5 H10 M8 11.5 V14.5"/></svg>
      <p>mdelaney@dravik-example.ie<br>www.dravikautomation-example.com</p>
    </div>
  </section>

</main>
</body>
</html>
```